Branvique needs a business Card Design

We are looking for a business card Design for our new Managed Service Provider Company, Branvique. Branvique encompasses everything IT for the average medium sized business. Our primary services are help desk support, cyber-security (malware and ransomware protection), and Disaster Recovery systems. We would like the design to have a very clean and professional look, with a very minimalist feel.

Target Market(s)

Medium to large sized businesses

Industry/Entity Type

It Service

Contact Information for Business Card

Name GoesHere
name@branvique.com
O: 555-382-6047
C: 555-731-5820

Font styles to use
Other font styles liked:
• Poppins Font Only Please

Colors

Designer to choose only greyscale colors for use in the design.

Requirements
Must have
• Logo included
Nice to have
• Cutting Edge, innovative, minimalistic, elegant

```html
<!DOCTYPE html>
<html lang="en">
<head>
<meta charset="utf-8">
<title>Branvique Business Card</title>
<link href="https://fonts.googleapis.com/css2?family=Poppins:wght@400;500&display=swap" rel="stylesheet">
<style>
  :root {
    --backdrop: #808080;
    --charcoal: #222426;
    --paper: #ffffff;
    --ink: #222426;
  }
  * { margin: 0; padding: 0; box-sizing: border-box; }
  html, body { width: 1200px; height: 1020px; overflow: hidden; }
  body {
    background: var(--backdrop);
    font-family: "Poppins", sans-serif;
    position: relative;
  }
  .card {
    position: absolute;
    width: 656px;
    height: 376px;
    border-radius: 26px;
    overflow: hidden;
  }
  .card--front { left: 272px; top: 88px; background: var(--charcoal); }
  .card--back { left: 271px; top: 514px; background: var(--paper); }

  .brand-dot {
    position: absolute;
    border-radius: 50%;
  }
  .card--front .brand-dot {
    width: 64px; height: 64px;
    left: 296px; top: 128px;
    background: var(--paper);
  }
  .card--back .brand-dot {
    width: 50px; height: 50px;
    left: 169px; top: 140px;
    background: var(--ink);
  }

  .wordmark {
    position: absolute;
    font-family: "Poppins", sans-serif;
    font-weight: 400;
    letter-spacing: 0.42em;
    white-space: nowrap;
  }
  .card--front .wordmark {
    left: 0; right: 0;
    top: 232px;
    text-align: center;
    font-size: 32px;
    color: var(--paper);
    padding-left: 0.42em;
  }
  .card--back .wordmark {
    left: 80px;
    top: 219px;
    font-size: 25px;
    color: var(--ink);
  }
  .divider {
    position: absolute;
    left: 327px;
    top: 125px;
    width: 2px;
    height: 126px;
    background: var(--ink);
  }
  .contact {
    position: absolute;
    left: 341px;
    top: 119px;
    color: var(--ink);
  }
  .contact__name {
    font-size: 25px;
    font-weight: 500;
    line-height: 1.2;
    margin-bottom: 10px;
    letter-spacing: 0.01em;
  }
  .contact__list { list-style: none; }
  .contact__item {
    display: flex;
    align-items: center;
    gap: 7px;
    font-size: 19px;
    line-height: 24px;
    letter-spacing: 0.01em;
  }
  .contact__icon { width: 13px; height: 13px; flex: none; }
</style>
</head>
<body>
  <section class="card card--front">
    <span class="brand-dot"></span>
    <div class="wordmark">BRANVIQUE</div>
  </section>

  <section class="card card--back">
    <span class="brand-dot"></span>
    <div class="wordmark">BRANVIQUE</div>
    <div class="divider"></div>
    <div class="contact">
      <p class="contact__name">Goes Here</p>
      <ul class="contact__list">
        <li class="contact__item">
          <svg class="contact__icon" viewBox="0 0 12 12"><rect x="2.5" y="0.8" width="7" height="10.4" rx="1.2" fill="none" stroke="#222426" stroke-width="1.4"/><circle cx="6" cy="9.2" r="0.7" fill="#222426"/></svg>
          555-731-5820
        </li>
        <li class="contact__item">
          <svg class="contact__icon" viewBox="0 0 12 12"><path d="M2.2 1.2l2 0 .8 2.4-1.3 1a6.5 6.5 0 0 0 3.5 3.5l1-1.3 2.4.8 0 2A1 1 0 0 1 9.6 10.8 9 9 0 0 1 1.2 2.4 1 1 0 0 1 2.2 1.2z" fill="#222426"/></svg>
          555-382-6047
        </li>
        <li class="contact__item">
          <svg class="contact__icon" viewBox="0 0 12 12"><rect x="0.5" y="2.2" width="11" height="7.6" fill="#222426"/><path d="M1 2.8l5 3.6 5-3.6" fill="none" stroke="#fff" stroke-width="1"/></svg>
          name@branvique.com
        </li>
        <li class="contact__item">
          <svg class="contact__icon" viewBox="0 0 12 12"><circle cx="6" cy="6" r="5.4" fill="#222426"/><path d="M3 4.2c1 .2 1.5 1 2.4.8.6 1 .2 2-.6 2.6M7.5 8.8c.2-1 1-1.4 1.8-1.4" fill="none" stroke="#fff" stroke-width="0.9"/></svg>
          www.branvique.com
        </li>
      </ul>
    </div>
  </section>
</body>
</html>
```